Can you create a Business Card based on the Logo you designed.

See example and would like to see other examples.

Trying to keep it very clean with a focus on the logo and name.

```html
<!DOCTYPE html>
<html lang="en">
<head>
<meta charset="utf-8">
<title>Graneva Business Card</title>
<link href="https://fonts.googleapis.com/css2?family=Montserrat:wght@400;600;700&display=swap" rel="stylesheet">
<style>
  :root {
    --backdrop: #1b1b1b;
    --paper: #f4f4f3;
    --brand-green: #0e6b3d;
    --leaf-green: #7cb940;
    --deep-green: #0f7a45;
    --accent-orange: #ee9a38;
    --ink: #2a2a2a;
    --white: #ffffff;
  }
  * { margin: 0; padding: 0; box-sizing: border-box; }
  html, body {
    width: 1200px;
    height: 1059px;
    overflow: hidden;
    background: var(--backdrop);
    font-family: "Montserrat", sans-serif;
  }
  .card {
    position: absolute;
    left: 255px;
    width: 690px;
    height: 392px;
    border-radius: 18px;
    overflow: hidden;
  }
  .card--front { top: 89px; background: var(--paper); }
  .card--back {
    top: 547px;
    background: linear-gradient(100deg, var(--deep-green) 10%, #3a8f48 50%, var(--leaf-green) 100%);
  }
  .wordmark {
    position: absolute;
    font-weight: 600;
    letter-spacing: 0.5px;
    line-height: 1;
    text-align: center;
    white-space: nowrap;
  }
  .card--front .wordmark {
    left: 34px;
    width: 330px;
    top: 172px;
    font-size: 52px;
    color: var(--brand-green);
  }
  .divider {
    position: absolute;
    left: 343px;
    top: 122px;
    width: 1.5px;
    height: 146px;
    background: var(--accent-orange);
  }
  .identity {
    position: absolute;
    left: 375px;
    top: 118px;
  }
  .identity__name {
    font-size: 26px;
    font-weight: 700;
    color: var(--brand-green);
    line-height: 1.1;
  }
  .identity__title {
    font-size: 16px;
    font-weight: 400;
    color: var(--ink);
    letter-spacing: 0.3px;
    margin-top: 1px;
  }
  .contacts {
    position: absolute;
    left: 378px;
    top: 192px;
    list-style: none;
  }
  .contacts li {
    display: flex;
    align-items: center;
    height: 28px;
    font-size: 17px;
    color: var(--ink);
    letter-spacing: 0.3px;
  }
  .contacts svg { width: 12px; height: 12px; margin-right: 8px; fill: var(--leaf-green); }
  .contacts .domain { color: var(--brand-green); }
  .card--back .wordmark {
    left: 0;
    right: 0;
    top: 178px;
    font-size: 78px;
    color: var(--white);
  }
</style>
</head>
<body>
  <section class="card card--front">
    <div class="wordmark">Graneva</div>
    <div class="divider"></div>
    <div class="identity">
      <p class="identity__name">Marcus Ellery</p>
      <p class="identity__title">Chief Executive Officer</p>
    </div>
    <ul class="contacts">
      <li>
        <svg viewBox="0 0 12 12" aria-hidden="true"><path d="M1 4c0-2 2-2.5 5-2.5S11 2 11 4v1H8.5V4h-5v1H1z M2.5 6h7l1 4.5h-9z"/></svg>
        +1 (555) 014-2290
      </li>
      <li>
        <svg viewBox="0 0 12 12" aria-hidden="true"><path d="M1 5l5-4 5 4v6H1z M2 5.6v4.6l3-2.3z M10 5.6v4.6l-3-2.3z"/></svg>
        CEO@graneva.com
      </li>
      <li>
        <svg viewBox="0 0 12 12" aria-hidden="true"><circle cx="6" cy="6" r="5.5"/></svg>
        www.<span class="domain">graneva</span>.com
      </li>
    </ul>
  </section>

  <section class="card card--back">
    <div class="wordmark">Graneva</div>
  </section>
</body>
</html>
```